Infographics for Zelmora

Zelmora company specializes in providing services for the organization of low-budget crowdsourcing research.
Crowdsourcing research - the solution of the problem by lots of people on a competitive basis. Types of research will not be limited to the design competition, and will cover all areas of economic activity.

The site contains the following sections: directory of research, user communities, where they can organize the communication according to common interests, forum, news ticker.

The site will feature two groups of users:
1. Organizers of commercial research - the firm or individual businessmen
2. Researchers of commercial research. Moreover, the organizers can act as executors in the research organized by other users.

Motives Organizers of research:
1. Solving business problems quickly and inexpensively, and the variability of solutions.
2. The possibility of recruiting the best researchers.
3. Self-promotion (positioning your company as an innovative, using cutting-edge technology solutions).
4. Doing Business with the times.

The motives of researchers:
1. Earnings with their knowledge by participating in competitions and receive the prize fund.
2. Employability organized research (if the customer makes an offer the researcher).
3. Intelligent Leisure
4. Communication: forum, chat with the professionals of their field of study.

Required:
Graphically show the behavior of two groups of people based on their motives.
Schematically, the sheet should be divided into two parts - the left diagram of the model of the organizers, to the right - the researchers. The middle - it is desirable that part where the researchers will provide solutions to problems of the organizers - the scheme intersect each other graphically.
This work will be used for placement on the website of the company, as well as in printed promotional products.

Target Market(s)

Entrepreneurs, businesses as well as economically active population of Russia

Industry/Entity Type

Communication

Requirements
Must have
• The company's logo from the attached file.
All decals made with cursive. All decails are editable.
The source file in vector format EPS.
Nice to have
• The color scheme of the site will match the logo, so it is desirable that the figure used the same color as the logo: black, gray, green. In an attachment, "firm color" color settings in the CMYK.
Schemes must come from the top down, page orientation - portrait.
Should not have
• Do not use photos. Only pictures.

```html
<!DOCTYPE html>
<html lang="en">
<head>
<meta charset="utf-8">
<title>Zelmora — Crowdsourcing Research Infographic</title>
<link rel="stylesheet" href="https://fonts.googleapis.com/css2?family=Cinzel:wght@700&family=Arimo:wght@700&display=swap">
<style>
  :root {
    --green: #7cc35a;
    --green-dark: #6aa94b;
    --black: #111111;
    --side-bg: #e2e2e2;
    --mid-bg: #ededed;
    --text: #111111;
    --logo-grey: #555555;
    --white: #ffffff;
  }
  html, body { margin: 0; padding: 0; overflow: hidden; }
  body { width: 900px; height: 1200px; }
  .canvas {
    position: relative;
    width: 900px;
    height: 1200px;
    overflow: hidden;
    background: var(--side-bg);
    font-family: "Arimo", Arial, sans-serif;
    font-weight: 700;
    color: var(--text);
  }
  .column-middle {
    position: absolute; left: 299px; top: 0; width: 301px; height: 1200px;
    background: var(--mid-bg);
  }
  .flow { position: absolute; left: 0; top: 0; }
  .intro-panel {
    position: absolute; left: 0; top: 0; width: 299px; height: 264px;
    background: var(--green);
  }
  .brand-title {
    position: absolute; left: 30px; top: 38px; margin: 0;
    font-family: "Cinzel", "Times New Roman", serif;
    font-size: 38px; letter-spacing: 1px; color: var(--white);
    text-shadow: 2px 2px 3px rgba(0,0,0,.7);
  }
  .intro-text {
    position: absolute; left: 39px; top: 122px; margin: 0;
    font-size: 25px; line-height: 30px; color: var(--white);
  }
  .motive {
    position: absolute; width: 280px;
    padding-left: 41px;
  }
  .motive .icon { position: absolute; left: 0; top: 4px; width: 32px; height: 32px; }
  .motive h3 { margin: 0; font-size: 18px; line-height: 20px; color: var(--green); }
  .motive p { margin: 0; font-size: 15px; line-height: 18.8px; }
  .stage-label {
    position: absolute; width: 130px; margin: 0; text-align: center;
    font-size: 17px; line-height: 23px;
    text-shadow: 0 0 3px var(--white), 0 0 3px var(--white);
  }
  .illustration { position: absolute; border-radius: 50%; }
  .idea-head {
    left: 313px; top: 125px; width: 257px; height: 222px;
    border-radius: 45% 50% 30% 40%;
    background: radial-gradient(circle at 55% 40%, #f4f0dc 0 18%, #a89c84 50%, #8a7f6a 100%);
    opacity: .85;
  }
  .achiever {
    left: 355px; top: 820px; width: 200px; height: 330px;
    border-radius: 40% 40% 20% 20%;
    background: linear-gradient(180deg, #f6f6f6 0%, #dcdcdc 55%, #8fcf6c 56%, #7cc35a 70%, #d8d8d8 71%, #cfcfcf 100%);
  }
  .powered-by {
    position: absolute; left: 607px; top: 932px; margin: 0;
    font-size: 23px; letter-spacing: 1px; color: var(--green);
  }
  .brand-name {
    position: absolute; left: 612px; top: 980px; margin: 0;
    font-size: 68px; font-weight: 700; color: var(--logo-grey);
  }
</style>
</head>
<body>
<main class="canvas">
  <div class="column-middle"></div>

  <svg class="flow" width="900" height="1200" viewBox="0 0 648 864" aria-hidden="true">
    <defs>
      <linearGradient id="stage-fill" x1="0" y1="0" x2="0" y2="1">
        <stop offset="0" stop-color="#f5f5f5"/>
        <stop offset="1" stop-color="#b9b9b9"/>
      </linearGradient>
    </defs>
    <!-- stage ovals -->
    <ellipse cx="538" cy="222" rx="48" ry="78" fill="#9a9a9a"/>
    <ellipse cx="533" cy="222" rx="46" ry="76" fill="url(#stage-fill)"/>
    <ellipse cx="333" cy="428" rx="50" ry="80" fill="#9a9a9a"/>
    <ellipse cx="328" cy="428" rx="48" ry="78" fill="url(#stage-fill)"/>
    <ellipse cx="120" cy="672" rx="48" ry="80" fill="#9a9a9a"/>
    <ellipse cx="115" cy="672" rx="46" ry="78" fill="url(#stage-fill)"/>

    <!-- researchers: black top band -->
    <path d="M648,95 L565,95 C505,95 472,135 472,205" fill="none" stroke="#111" stroke-width="34"/>
    <polygon points="446,200 498,200 472,245" fill="#111"/>

    <!-- green band from researchers to solutions -->
    <path d="M598,180 C598,280 570,318 505,318 L375,318 C315,318 270,360 268,455" fill="none" stroke="#7cc35a" stroke-width="30"/>
    <polygon points="575,185 621,185 600,140" fill="#7cc35a"/>
    <polygon points="244,450 292,450 268,495" fill="#7cc35a"/>

    <!-- black band from solutions to organizers -->
    <path d="M383,440 C383,510 355,552 290,552 L115,552 C62,552 45,600 45,690" fill="none" stroke="#111" stroke-width="34"/>
    <polygon points="360,442 408,442 384,400" fill="#111"/>
    <polygon points="20,688 70,688 45,733" fill="#111"/>

    <!-- green exit band -->
    <path d="M168,640 C168,745 140,785 80,785 L0,785" fill="none" stroke="#7cc35a" stroke-width="30"/>
    <polygon points="145,645 191,645 170,602" fill="#7cc35a"/>
  </svg>

  <section class="intro-panel">
    <h1 class="brand-title">ZELMORA</h1>
    <p class="intro-text">Intro text<br>will be placed<br>here</p>
  </section>

  <div class="illustration idea-head" role="img" aria-label="Head silhouette made of small idea icons around a light bulb"></div>

  <section class="motives-organizers">
    <div class="motive" style="left:21px;top:330px">
      <svg class="icon" viewBox="0 0 32 32"><g stroke="#4f8a37" stroke-width="3" stroke-linecap="round"><line x1="16" y1="3" x2="16" y2="29"/><line x1="4.7" y1="9.5" x2="27.3" y2="22.5"/><line x1="4.7" y1="22.5" x2="27.3" y2="9.5"/></g></svg>
      <h3>TITLE</h3>
      <p>Required textRequired text<br>Required textRequired text<br>Required textRequired text</p>
    </div>
    <div class="motive" style="left:21px;top:416px">
      <svg class="icon" viewBox="0 0 32 32"><g stroke="#4f8a37" stroke-width="3" stroke-linecap="round"><line x1="16" y1="3" x2="16" y2="29"/><line x1="4.7" y1="9.5" x2="27.3" y2="22.5"/><line x1="4.7" y1="22.5" x2="27.3" y2="9.5"/></g></svg>
      <h3>TITLE</h3>
      <p>Required textRequired text<br>Required textRequired text<br>Required textRequired text</p>
    </div>
    <div class="motive" style="left:21px;top:500px">
      <svg class="icon" viewBox="0 0 32 32"><g stroke="#4f8a37" stroke-width="3" stroke-linecap="round"><line x1="16" y1="3" x2="16" y2="29"/><line x1="4.7" y1="9.5" x2="27.3" y2="22.5"/><line x1="4.7" y1="22.5" x2="27.3" y2="9.5"/></g></svg>
      <h3>TITLE</h3>
      <p>Required textRequired text<br>Required textRequired text<br>Required textRequired text</p>
    </div>
    <div class="motive" style="left:21px;top:583px">
      <svg class="icon" viewBox="0 0 32 32"><g stroke="#4f8a37" stroke-width="3" stroke-linecap="round"><line x1="16" y1="3" x2="16" y2="29"/><line x1="4.7" y1="9.5" x2="27.3" y2="22.5"/><line x1="4.7" y1="22.5" x2="27.3" y2="9.5"/></g></svg>
      <h3>TITLE</h3>
      <p>Required textRequired text<br>Required textRequired text<br>Required textRequired text</p>
    </div>
  </section>

  <section class="motives-researchers">
    <div class="motive" style="left:604px;top:539px">
      <svg class="icon" viewBox="0 0 32 32"><g stroke="#4f8a37" stroke-width="3" stroke-linecap="round"><line x1="16" y1="3" x2="16" y2="29"/><line x1="4.7" y1="9.5" x2="27.3" y2="22.5"/><line x1="4.7" y1="22.5" x2="27.3" y2="9.5"/></g></svg>
      <h3>TITLE</h3>
      <p>Required textRequired text<br>Required textRequired text<br>Required textRequired text</p>
    </div>
    <div class="motive" style="left:604px;top:625px">
      <svg class="icon" viewBox="0 0 32 32"><g stroke="#4f8a37" stroke-width="3" stroke-linecap="round"><line x1="16" y1="3" x2="16" y2="29"/><line x1="4.7" y1="9.5" x2="27.3" y2="22.5"/><line x1="4.7" y1="22.5" x2="27.3" y2="9.5"/></g></svg>
      <h3>TITLE</h3>
      <p>Required textRequired text<br>Required textRequired text<br>Required textRequired text</p>
    </div>
    <div class="motive" style="left:604px;top:708px">
      <svg class="icon" viewBox="0 0 32 32"><g stroke="#4f8a37" stroke-width="3" stroke-linecap="round"><line x1="16" y1="3" x2="16" y2="29"/><line x1="4.7" y1="9.5" x2="27.3" y2="22.5"/><line x1="4.7" y1="22.5" x2="27.3" y2="9.5"/></g></svg>
      <h3>TITLE</h3>
      <p>Required textRequired text<br>Required textRequired text<br>Required textRequired text</p>
    </div>
    <div class="motive" style="left:604px;top:792px">
      <svg class="icon" viewBox="0 0 32 32"><g stroke="#4f8a37" stroke-width="3" stroke-linecap="round"><line x1="16" y1="3" x2="16" y2="29"/><line x1="4.7" y1="9.5" x2="27.3" y2="22.5"/><line x1="4.7" y1="22.5" x2="27.3" y2="9.5"/></g></svg>
      <h3>TITLE</h3>
      <p>Required textRequired text<br>Required textRequired text<br>Required textRequired text</p>
    </div>
  </section>

  <p class="stage-label" style="left:682px;top:226px">the<br>researchers<br>part<br>title<br>goes<br>here</p>
  <p class="stage-label" style="left:391px;top:534px">researchers<br>will<br>provide<br>solutions<br>in<br>this<br>part</p>
  <p class="stage-label" style="left:92px;top:862px">model<br>of<br>the<br>organizers<br>part<br>title</p>

  <div class="illustration achiever" role="img" aria-label="Figure holding a large green check mark"></div>

  <p class="powered-by">POWERED BY :</p>
  <p class="brand-name">Zelmora</p>
</main>
</body>
</html>
```